Stationary for Keeping Steady

we are in the process of creating a more professional image for our company Keeping Steady Paramedical Services. We have recently had a new logo and general brochure designed using artpitchhub and have been impressed by the quality of submissions.

We need:
- Letterhead (A4)
- Business Cards
- With compliments slips
- Email stationary

Letterhead information:
Address - 47 Wattlebrook Drive, Fernhollow Vic 3091
Phone - 1800 462 817
email - enquiries@keepsteady.com.au
Internet - www.keepsteady.com.au
ABN - 82 463 915 207
ACN - 264 871 035

Files need to be able to be edited in Illustrator CS2

Business Cards / with compliments slips / email stationary:
Double sided.
One side to have Name, Mobile number, company phone 1800462817, email, internet address

Files need to be able to be edited in Illustrator CS2 (except email stationary)

Our website is www.keepsteady.com.au for more information. Do not base designs on the website as it will eventually be revised.

Target Market(s)

Australian based businesses, government departments and schools. We specialise in corporate customers rather than public first aid course

Industry/Entity Type

Internet

Requirements
Must have
• Where applicable file to be editable in illustrator CS2 to allow future alterations.

```html
<!DOCTYPE html>
<html lang="en">
<head>
<meta charset="utf-8">
<title>Keeping Steady Paramedical Services – Letterhead</title>
<link href="https://fonts.googleapis.com/css2?family=Questrial&family=Open+Sans:wght@600&display=swap" rel="stylesheet">
<style>
  :root {
    --brand-red: #c0161f;
    --brand-red-soft: #f2a7aa;
    --ink: #111111;
    --ink-grey: #3a3a3a;
    --page: #ffffff;
    --page-edge: #8a6f78;
    --ribbon-grey: #9a9a9a;
  }
  html, body {
    margin: 0;
    padding: 0;
    width: 941px;
    height: 1200px;
    overflow: hidden;
    background: #ffffff;
  }
  .canvas {
    position: relative;
    width: 941px;
    height: 1200px;
    overflow: hidden;
  }
  .artwork {
    position: absolute;
    inset: 0;
    width: 941px;
    height: 1200px;
  }
  .brand-mark {
    position: absolute;
    left: 205px;
    top: 86px;
    width: 92px;
    height: 92px;
    background: var(--brand-red);
  }
  .company-name {
    position: absolute;
    left: 346px;
    top: 80px;
    margin: 0;
    font-family: "Questrial", sans-serif;
    font-size: 56px;
    font-weight: 400;
    line-height: 1;
    color: var(--brand-red);
    letter-spacing: 0.5px;
    white-space: nowrap;
  }
  .company-tagline {
    position: absolute;
    left: 348px;
    top: 138px;
    margin: 0;
    font-family: "Questrial", sans-serif;
    font-size: 24px;
    line-height: 1;
    color: var(--ink-grey);
    white-space: nowrap;
  }
  .contact-details {
    position: absolute;
    left: 300px;
    top: 168px;
    width: 480px;
    margin: 0;
    font-family: "Open Sans", sans-serif;
    font-weight: 600;
    font-size: 12.5px;
    line-height: 17px;
    color: var(--ink);
    text-align: center;
    font-style: normal;
  }
  .contact-details span + span { margin-left: 14px; }
  .footer-ribbon {
    position: absolute;
    left: 101px;
    top: 1040px;
    width: 733px;
    height: 68px;
    background: linear-gradient(90deg, #e9e9e9 0%, #f6d2d4 25%, #ececec 50%, #f6d2d4 75%, #e4e4e4 100%);
  }
</style>
</head>
<body>
<div class="canvas">
  <svg class="artwork" viewBox="0 0 764 970" preserveAspectRatio="none" aria-hidden="true">
    <defs>
      <linearGradient id="pinkSweepTop" x1="0" y1="0" x2="1" y2="1">
        <stop offset="0" stop-color="#fbe1e2"/>
        <stop offset="0.6" stop-color="#f19ea2"/>
        <stop offset="1" stop-color="#f4b5b8"/>
      </linearGradient>
      <linearGradient id="pinkSweepBottom" x1="1" y1="0" x2="0" y2="1">
        <stop offset="0" stop-color="#f19ea2"/>
        <stop offset="1" stop-color="#fde9ea"/>
      </linearGradient>
      <linearGradient id="greyRibbon" x1="0" y1="0" x2="0" y2="1">
        <stop offset="0" stop-color="#bdbdbd"/>
        <stop offset="0.4" stop-color="#e8e8e8"/>
        <stop offset="0.7" stop-color="#c9c9c9"/>
        <stop offset="1" stop-color="#9a9a9a"/>
      </linearGradient>
      <linearGradient id="pinkRibbon" x1="0" y1="0" x2="0" y2="1">
        <stop offset="0" stop-color="#ffffff" stop-opacity="0"/>
        <stop offset="0.4" stop-color="#f3a9ac"/>
        <stop offset="1" stop-color="#e2787d"/>
      </linearGradient>
      <linearGradient id="headerSwoosh" x1="0" y1="0" x2="1" y2="0">
        <stop offset="0" stop-color="#8e0e15"/>
        <stop offset="0.5" stop-color="#c0161f"/>
        <stop offset="1" stop-color="#d8262f"/>
      </linearGradient>
    </defs>

    <!-- background sweeps -->
    <path d="M520 0 C640 10 760 20 764 60 C770 170 730 290 678 385 L678 120 C650 60 590 20 520 0 Z" fill="url(#pinkSweepTop)"/>
    <path d="M82 590 C40 700 10 820 40 930 C55 960 80 970 110 968 C60 920 40 820 82 700 Z" fill="url(#pinkSweepBottom)"/>

    <!-- page -->
    <rect x="82" y="60" width="595" height="841" fill="#ffffff" stroke="#8a6f78" stroke-width="1"/>

    <!-- vertical ribbon -->
    <path d="M335 200 C370 260 385 330 385 400 C385 470 395 540 440 640 C500 770 580 850 660 895 C580 840 520 760 470 640 C420 520 405 440 400 380 C395 300 370 240 335 200 Z" fill="url(#greyRibbon)" opacity="0.85"/>
    <path d="M380 380 C385 470 395 560 430 650 C470 750 520 820 560 870 C505 800 460 720 430 640 C400 560 388 460 380 380 Z" fill="url(#pinkRibbon)" opacity="0.8"/>

    <!-- header swoosh -->
    <path d="M88 100 C60 150 140 200 330 208 C480 214 600 198 672 175 C560 196 420 204 300 196 C150 186 80 150 88 100 Z" fill="#111111"/>
    <path d="M86 98 C70 140 150 180 330 188 C480 193 600 186 672 175 C560 186 420 190 300 182 C160 172 92 140 86 98 Z" fill="url(#headerSwoosh)"/>
  </svg>

  <div class="brand-mark"></div>
  <h1 class="company-name">Keeping Steady</h1>
  <p class="company-tagline">Paramedical Services Pty Ltd</p>
  <address class="contact-details">
    <span>Phone - 1800 462 817</span><span>ABN - 82 463 915 207</span><span>ACN - 264 871 035</span><br>
    email - enquiries@keepsteady.com.au - www.keepsteady.com.au<br>
    Address - 47 Wattlebrook Drive, Fernhollow Vic 3091
  </address>

  <div class="footer-ribbon" role="img" aria-label="Decorative footer band: a grey ribbon weaving through a row of repeated brand symbols in red and black"></div>
</div>
</body>
</html>
```